Mixed Martial Arts Gym Needs a general info flyer

8.5x11
2 sided
Colors: Compliment our logo (attached) Dark Gray, Light Gray, White, Black, Red.
I would like the front of the general info flyer to talk about our general information, listing the offerings bulleted below as well as our address, phone # website etc.
I would also like to highlight that we have relocated to Choctaw, OK as well as mention the owner, head instructor Dale Wenrick: PKL Featherweight veteran, Harlow County Police Officer and Redbud Grappling standout.
We would like a general flyer that talks about our general offerings along with a few pictures. We are a mixed martial arts gym we have moved to a new location in Choctaw, OK. You can find a lot of info on our gym at our website www.k7fightworks-example.com I've attached pictures as well as an example of a few flyers I like.

This info should be included on front of flyer:
• Adult MMA
• Boxing
• Strength & Conditioning
• Brazilian Jiu Jitsu
• No-Gi Jiu-Jitsu
• Women’s Cardio Kickboxing

• Youth Program: Ages 7-14
Teaching disciplines in Jiu-Jitsu, Judo,
Wrestling, Self-defense

*see our website for rates and our current schedule

We also offer a full fitness facility - Iron Lark Fitness - with free weights, cardio & cable machines, personal training and fitness classes.
Discounts for Military, Law Enforcement, Fire and College Students.

ON THE BACK OF FLYER:
I would like to include a brief description of each of our classes and an about us. You can find all of that info on our website www.k7fightworks-example.com as well as pictures.

```html
<!DOCTYPE html>
<html lang="en">
<head>
<meta charset="utf-8">
<title>Fightworks – Classes</title>
<link rel="stylesheet" href="https://fonts.googleapis.com/css2?family=Oswald:wght@400;500&family=Arimo:wght@400;700&display=swap">
<style>
  :root {
    --stage: #4b4b4b;
    --sheet: #1c1c1c;
    --sheet-deep: #121212;
    --steel-light: #cfcfcf;
    --steel-dark: #8d8d8d;
    --red: #c8201f;
    --wine: #6a0e1a;
    --ink: #d9d9d9;
    --white: #ffffff;
    --panel-top: #4c4c4c;
    --panel-bottom: #2a2a2a;
  }
  * { box-sizing: border-box; margin: 0; padding: 0; }
  html, body { width: 1200px; height: 1000px; overflow: hidden; }
  body { background: var(--stage); position: relative; font-family: "Arimo", Arial, sans-serif; }

  .flyer {
    position: absolute; left: 258px; top: 58px; width: 684px; height: 879px;
    background: radial-gradient(ellipse at 50% 40%, var(--sheet) 0%, var(--sheet-deep) 100%);
    overflow: hidden; box-shadow: 0 6px 24px rgba(0,0,0,.5);
  }
  .header-band { position: absolute; left: 0; top: 0; width: 684px; height: 64px; }
  .header-title {
    position: absolute; right: 28px; top: 12px;
    font-family: "Oswald", "Arial Narrow", sans-serif; font-weight: 500;
    font-size: 29px; color: var(--white); letter-spacing: .5px;
  }

  .class-block {
    position: absolute; width: 302px;
    font-size: 11px; line-height: 12.3px; color: var(--ink); text-align: justify;
  }
  .class-block p { margin-bottom: 12.3px; }
  .class-photo {
    float: left; width: 92px; height: 93px; margin: 0 14px 8px 0;
  }
  .class-title {
    font-family: "Oswald", "Arial Narrow", sans-serif; font-weight: 400;
    font-size: 16.5px; line-height: 18px; color: var(--red);
    margin-bottom: 2px; text-align: left; white-space: nowrap;
  }

  .block-bjj { left: 28px; top: 77px; }
  .block-mma { left: 28px; top: 249px; }
  .block-kick { left: 356px; top: 77px; }
  .block-boxing { left: 356px; top: 296px; }
  .block-kids { left: 356px; top: 514px; }

  .about-panel { position: absolute; left: 30px; top: 542px; width: 296px; height: 262px; }
  .about-shape { position: absolute; inset: 0; }
  .about-content { position: absolute; left: 12px; top: 34px; width: 274px; font-size: 11px; line-height: 12.3px; color: var(--ink); text-align: justify; }
  .about-title {
    font-family: "Oswald", "Arial Narrow", sans-serif; font-weight: 400;
    font-size: 33px; line-height: 38px; color: var(--red); margin-bottom: 8px; text-align: left;
  }
  .about-content p { margin-bottom: 12.3px; }

  .footer-band {
    position: absolute; left: 0; top: 802px; width: 684px; height: 77px;
    background: var(--wine);
  }
  .footer-schedule {
    position: absolute; left: 128px; top: 16px;
    font-size: 11px; line-height: 13px; font-weight: 700; color: var(--white);
  }
  .footer-offer {
    position: absolute; left: 361px; top: 14px; width: 300px;
    font-size: 11px; line-height: 13px; font-weight: 700; color: var(--white);
  }

  .brand-name {
    position: absolute; left: 22px; top: 22px; width: 96px;
    font-family: "Arimo", Arial, sans-serif; font-weight: 700; font-size: 15px; line-height: 18px;
    color: var(--white); white-space: nowrap;
  }
</style>
</head>
<body>
  <main class="flyer">
    <svg class="header-band" viewBox="0 0 684 64" aria-hidden="true">
      <defs>
        <linearGradient id="steel" x1="0" y1="0" x2="1" y2="0">
          <stop offset="0" stop-color="#cfcfcf"/>
          <stop offset="0.6" stop-color="#a9a9a9"/>
          <stop offset="1" stop-color="#8d8d8d"/>
        </linearGradient>
      </defs>
      <polygon points="0,0 684,0 684,62 0,28" fill="url(#steel)"/>
    </svg>
    <h1 class="header-title">CLASSES</h1>

    <section class="class-block block-bjj">
      <div class="class-photo" role="img" aria-label="Photo of grapplers training jiu-jitsu on blue and red mats" style="background:linear-gradient(135deg,#3c5fa8,#c9c2bd 55%,#7a2a2a)"></div>
      <h2 class="class-title">"Iron Tide" BRAZILIAN JIU JITSU</h2>
      <p>Our Jiu-Jitsu is led by Tomas Reyel. These classes are perfect for anyone who wants to learn what to do when the fight gets to the ground, increase your core strength, or simply get into the best shape of your life!</p>
      <p>The Brazilian Jiu-Jitsu program at Fightworks incorporates the traditions from Brazilian Jiu-Jitsu and the practicality of no-gi grappling ground training for self-defense, MMA, and sport Jiu-Jitsu.</p>
    </section>

    <section class="class-block block-mma">
      <div class="class-photo" role="img" aria-label="Photo of two fighters in gis grappling on the mat" style="background:linear-gradient(135deg,#6b4b3c,#d8d2cc 50%,#2a2a2a)"></div>
      <h2 class="class-title">MIXED MARTIAL ARTS</h2>
      <p>Our Mixed Martial Arts classes allow students to possess a well-rounded skill for both striking and ground.</p>
      <p>Students of all skill levels are welcome to participate in this fun, intriguing fighting style. Our classes are for everyone, not just our professional and amateur fighters.</p>
      <p>Our programs our designed to take even the most inexperienced student and equip them with the tools necessary for self-defense and extreme physical fitness. Our MMA students learn a variety of different styles including Brazilian Jiu Jitsu, Wrestling, Kickboxing, and Boxing to make them a well-rounded, powerful athlete.</p>
      <p>Our MMA programs will get you fit, confident and healthy while learning a combination of techniques and strategies so you can set and reach any goal you set your mind to.</p>
    </section>

    <div class="about-panel">
      <svg class="about-shape" viewBox="0 0 296 262" aria-hidden="true">
        <defs>
          <linearGradient id="panel" x1="0" y1="0" x2="0" y2="1">
            <stop offset="0" stop-color="#4c4c4c"/>
            <stop offset="1" stop-color="#2a2a2a"/>
          </linearGradient>
        </defs>
        <polygon points="0,0 296,30 296,262 0,262" fill="url(#panel)"/>
      </svg>
      <div class="about-content">
        <h2 class="about-title">ABOUT US</h2>
        <p>Fightworks is a dynamic training facility with state-of-the-art equipment, professional instructors, and high-level training. All of our classes are taught by professionals who have an abundance of skills and knowledge in many aspects of MMA.</p>
        <p>We are a tight knit, supportive community.</p>
        <p>Our focus is a fitness experience that builds a stronger you inside and out.</p>
      </div>
    </div>

    <section class="class-block block-kick">
      <div class="class-photo" role="img" aria-label="Photo of women hitting focus mitts in kickboxing class" style="background:linear-gradient(135deg,#8a6a5a,#e8e2de 50%,#a32a2a)"></div>
      <h2 class="class-title">WOMEN'S KICKBOXING</h2>
      <p>The class focuses on improving body composition, hand-eye coordination, cardiovascular health as well as developing self-confidence and an awareness for self-defense.</p>
      <p style="clear:both">This class is for all levels but if you love competition this class is for you! Our classes consist of high intensity workouts (high reps, in short bursts of time), followed by a cardiovascular workout consisting of jabs, hooks, uppercuts and kicks designed to get you on your way to a leaner you and a healthier state of mind. Hitting the focus mitts is not only a great workout but also intellectually stimulating, and FUN!</p>
    </section>

    <section class="class-block block-boxing">
      <div class="class-photo" role="img" aria-label="Photo of an athlete kicking a heavy bag in a dark gym" style="background:linear-gradient(135deg,#1a1a1a,#5a5a5a 55%,#2a2a2a)"></div>
      <h2 class="class-title">BOXING &amp; STRIKING</h2>
      <p>Our boxing classes can increase endurance, strength and speed. Striking coach Owen Saltry focuses on sound boxing fundamentals, solid-cardio conditioning and stretching. Boxing classes consist of heavy bag work, shadow boxing, focus mit drills as well as strength and conditioning techniques focused on increasing hand speed as well as hand eye coordination. Members jump rope, shadow box, circuit train, work various bags and do one-on-one pad work. Our workouts are designed to tone your entire body while honing your boxing skills in the rings. Athletes of all levels and experiences are welcome.</p>
    </section>

    <section class="class-block block-kids">
      <div class="class-photo" role="img" aria-label="Photo of a coach holding pads for a young student" style="background:linear-gradient(135deg,#3a3a3a,#b03030 55%,#2a2a2a)"></div>
      <h2 class="class-title">KIDS PROGRAM</h2>
      <p>Kids Classes combine disciplines such as: Beginner MMA, Wrestling, beginner no-gi Jiu-Jitsu and Sambo.</p>
      <p>An excellent way for children to learn valuable tools to handle life's many, for youth in need of structure and instability challenges-all while having a good time!</p>
      <p>We focus on building attitude, discipline, and respect in our students so they have an advantage in any athletics program and in every day life. Our classes are twice a week, 1 hour classes. Students are taught self-defense, self-confidence, and the value of hard work in a safe atmosphere organized and run by professionals.</p>
      <p>Our classes are a positive way for children to release stress, learn the importance of physical fitness, and feel accomplishment after earning achievement.</p>
    </section>

    <footer class="footer-band">
      <p class="brand-name">Fightworks</p>
      <p class="footer-schedule">For schedules, please visit<br>www.k7fightworks-example.com</p>
      <p class="footer-offer">We encourage anyone to take a FREE CLASS to see just how friendly and worthwhile the experience will be!</p>
    </footer>
  </main>
</body>
</html>
```